Postcard/Poster design for Feature film

I'm just wrapping post-production on my indie first feature, and I'm going to be attending some big festivals over the next few months to promote my film by handing out postcards.

I'll also be needing posters for festivals that I'll get into.

The name of my film is Nettle Winter, and it's a melancholic drama about one woman's desperate need for a male child.
I have a still photo from the film that I'd like to use on the poster and postcard.
Updates

The postcard design should take into consideration the fact that a postcard has two sides. All the info doesnt have to on the front. Therefore the post card design should be two designs, the front and the back.
Take a look at a real postcard for inspiration.

Target Market(s)

The arthouse film loving types.

Requirements
Must have
• The design must have the still photo from the film, the name of the film, Nettle Winter, and all the other logo's at the bottom.
There are other logos that I'm unable to attach because I reached the limit, but I can send those later.

The postcard design should take into consideration the fact that a postcard has two sides. All the info doesn't have to be on the front of the card. Therefore the post card design should be in two parts, the front and the back.

The postcard size is standard (4 x 6 inches).
Poster 40 inches (wide) x 30 inches (high).

The design must be 350dpi.

```html
<!DOCTYPE html>
<html lang="en">
<head>
<meta charset="utf-8">
<title>Nettle Winter — Poster and Postcard</title>
<link href="https://fonts.googleapis.com/css2?family=Courier+Prime:wght@400;700&family=Pathway+Gothic+One&display=swap" rel="stylesheet">
<style>
  :root {
    --page: #ffffff;
    --night: #0a0b1c;
    --navy: #1c1f45;
    --dusk: #4a4d86;
    --lilac: #a8a3c8;
    --haze: #e6e4f0;
    --title-blue: #5a78c0;
    --title-ink: #1b2350;
    --credit-light: #d9dbe8;
    --credit-dark: #2a2a33;
    --badge-light: #6f7180;
    --badge-dark: #8a8b94;
  }
  * { margin: 0; padding: 0; box-sizing: border-box; }
  html, body { width: 1200px; height: 878px; overflow: hidden; background: var(--page); }
  .canvas { position: relative; width: 1200px; height: 878px; }

  .title { font-family: "Courier Prime", "Courier New", monospace; line-height: 1; }
  .title .small { display: block; font-size: 44px; }
  .title .large { display: block; font-size: 72px; color: var(--title-blue); letter-spacing: -2px; }

  .credits {
    font-family: "Pathway Gothic One", "Arial Narrow", sans-serif;
    text-transform: uppercase;
    font-size: 9.5px;
    line-height: 12px;
    letter-spacing: 0.2px;
  }
  .credits .role { font-size: 6.5px; letter-spacing: 0.3px; }

  .badges { display: flex; gap: 22px; align-items: center; }
  .badge {
    display: flex; align-items: center; gap: 4px;
    font-family: "Pathway Gothic One", "Arial Narrow", sans-serif;
    font-size: 8px; text-transform: uppercase; letter-spacing: 0.4px;
  }
  .badge .mark { width: 7px; height: 7px; background: currentColor; }

  /* Poster */
  .poster {
    position: absolute; left: 28px; top: 30px; width: 579px; height: 818px;
    background: var(--night); overflow: hidden;
    box-shadow: 0 1px 4px rgba(0,0,0,0.25);
  }
  .poster-still {
    position: absolute; inset: 0;
    background:
      radial-gradient(ellipse 45% 40% at 85% 22%, var(--haze) 0%, rgba(230,228,240,0.6) 40%, transparent 75%),
      radial-gradient(ellipse 40% 35% at 60% 40%, var(--dusk) 0%, transparent 80%),
      linear-gradient(180deg, transparent 55%, var(--night) 92%),
      linear-gradient(90deg, var(--night) 0%, var(--navy) 30%, var(--dusk) 60%, var(--lilac) 100%);
  }
  .poster .title { position: absolute; left: 98px; top: 495px; color: #fff; }
  .poster .credits {
    position: absolute; left: 0; right: 0; top: 694px;
    text-align: center; color: var(--credit-light);
  }
  .poster .badges { position: absolute; left: 200px; top: 758px; color: var(--badge-light); }

  /* Postcard front */
  .card-front {
    position: absolute; left: 653px; top: 93px; width: 517px; height: 344px;
    background: var(--night); overflow: hidden;
    box-shadow: 0 1px 4px rgba(0,0,0,0.25);
  }
  .card-front-still {
    position: absolute; inset: 0;
    background:
      radial-gradient(ellipse 40% 45% at 18% 20%, var(--haze) 0%, rgba(230,228,240,0.5) 45%, transparent 80%),
      radial-gradient(ellipse 35% 40% at 45% 45%, var(--dusk) 0%, transparent 80%),
      linear-gradient(90deg, transparent 60%, var(--night) 88%),
      linear-gradient(0deg, var(--night) 0%, var(--navy) 35%, var(--dusk) 70%, var(--lilac) 100%);
  }
  .card-front .title {
    position: absolute; left: 380px; top: 310px;
    transform: rotate(-90deg); transform-origin: 0 0;
    color: #fff; white-space: nowrap;
  }
  .card-front .title .small { font-size: 34px; }
  .card-front .title .large { font-size: 56px; }

  /* Postcard back */
  .card-back {
    position: absolute; left: 653px; top: 458px; width: 517px; height: 345px;
    background: #fff;
    box-shadow: 0 1px 5px rgba(0,0,0,0.28);
  }
  .card-back .title { position: absolute; left: 48px; top: 38px; color: var(--title-ink); }
  .card-back .title .small { font-size: 40px; }
  .card-back .title .large { font-size: 66px; }
  .card-back .credits {
    position: absolute; left: 48px; top: 203px; width: 260px;
    color: var(--credit-dark); font-size: 9px; line-height: 11px;
  }
  .card-back .badges { position: absolute; left: 48px; top: 290px; color: var(--badge-dark); }
</style>
</head>
<body>
<main class="canvas">

  <section class="poster" aria-label="Festival poster">
    <div class="poster-still" role="img" aria-label="Film still: a woman in profile by a bright window, a child's arm wrapped around her neck, cool blue and lilac light"></div>
    <h1 class="title"><span class="small">Nettle</span><span class="large">Winter</span></h1>
    <div class="credits">
      <p>Pale Harbor Productions <span class="role">presents a film by</span> Adaeze Okoro &nbsp;'Nettle Winter' <span class="role">cinematographer</span> Marta Kowalik</p>
      <p><span class="role">production designer</span> Kofi Mensah Ade <span class="role">original music by</span> Lukas Brenner <span class="role">edited by</span> Paul Varenne <span class="role">executive producer</span> Nkem Obi</p>
      <p><span class="role">executive producers</span> Efe Ovie, Uche Ovie, Tunde Ovie, Kemi Ovie, Seun Adeyemi, Bisi Falana, Remi Falana</p>
      <p><span class="role">producer</span> Adaeze Okoro <span class="role">and</span> Tari Ovie <span class="role">director/writer</span> Adaeze Okoro</p>
    </div>
    <div class="badges">
      <span class="badge"><span class="mark"></span>Fondlab</span>
      <span class="badge"><span class="mark"></span>Lensworks</span>
      <span class="badge"><span class="mark"></span>Huemark</span>
    </div>
  </section>

  <section class="card-front" aria-label="Postcard front">
    <div class="card-front-still" role="img" aria-label="Film still: a woman leaning back by a window, a child's arm around her, cool blue and lilac light"></div>
    <h2 class="title"><span class="small">Nettle</span><span class="large">Winter</span></h2>
  </section>

  <section class="card-back" aria-label="Postcard back">
    <h2 class="title"><span class="small">Nettle</span><span class="large">Winter</span></h2>
    <div class="credits">
      <p>Pale Harbor Productions <span class="role">presents a film by</span> Adaeze Okoro 'Nettle Winter'</p>
      <p><span class="role">cinematographer</span> Marta Kowalik <span class="role">production designer</span> Kofi Mensah Ade</p>
      <p><span class="role">original music by</span> Lukas Brenner <span class="role">edited by</span> Paul Varenne <span class="role">executive producer</span> Nkem Obi</p>
      <p><span class="role">executive producers</span> Efe Ovie, Uche Ovie, Tunde Ovie, Kemi Ovie,</p>
      <p>Seun Adeyemi, Bisi Falana, Remi Falana <span class="role">producer</span> Adaeze Okoro</p>
      <p><span class="role">and</span> Tari Ovie <span class="role">director/writer</span> Adaeze Okoro</p>
    </div>
    <div class="badges">
      <span class="badge"><span class="mark"></span>Fondlab</span>
      <span class="badge"><span class="mark"></span>Lensworks</span>
      <span class="badge"><span class="mark"></span>Huemark</span>
    </div>
  </section>

</main>
</body>
</html>
```